HCW Business Card Design

I am a wedding and event Planner. I have just completed a name change from Gatherings by Odette to The Hollow Crest Workshop and I just received my new logo and need new business cards to match my new brand. Elegant, chic and upscale yet simple. I am drafting a new website on my old (for drafting purposes). You can take a look and it will give you an idea of the direction of my brand. (www.gatheringsbyodette.example). I would like gray and white colors and it can be a shaded mixture of grays. I am open in regard to placement of the information

Target Market(s)

Brides, Corporate Companies, Families etc.

Industry/Entity Type

Wedding

Contact Information for Business Card

The Hollow Crest Workshop
www.myhollowcrestworkshop.example
Event Planning and Design Firm
Odette M. Vance, Owner/CEO
Certified Event & Wedding Planner
T: (555) 240-7318 | F: (555) 617-4052
E: wegather@myhollowcrestworkshop.example
(please put T, E & F letters in a script font)

Gather with Care. Care to Share. Share the Joy. (rb)

(social icons instead of text)
twitter: @hollowcrestwork1
facebook: @thehollowcrestwork
Pinterest: @hollowcrestwork
instagram: @thehollowcrestwork1

Can we put a barcode leading to my website

```html
<!DOCTYPE html>
<html lang="en">
<head>
<meta charset="utf-8">
<title>HCW Business Card</title>
<link rel="stylesheet" href="https://fonts.googleapis.com/css2?family=Questrial&family=Pinyon+Script&display=swap">
<style>
  :root {
    --page: #e9e7e4;
    --wood-dark: #5f5f60;
    --wood-light: #8a8a8b;
    --card-white: #f8f7f4;
    --ink-gray: #7a7a7a;
    --ink-soft: #8e8e8e;
    --band-yellow: #f3f0a4;
    --amp-yellow: #d9d27a;
    --ornament-gray: #c9c9c9;
    --white: #ffffff;
  }
  * { box-sizing: border-box; margin: 0; padding: 0; }
  html, body {
    width: 1200px; height: 865px; overflow: hidden;
    background: var(--page);
    font-family: "Questrial", "Century Gothic", sans-serif;
  }
  .card {
    position: absolute; left: 240px; width: 720px; height: 411px;
    border-radius: 4px; overflow: hidden;
    box-shadow: 0 2px 8px rgba(0,0,0,0.18);
  }

  /* Front face */
  .card-front { top: 15px; }
  .wood-texture {
    position: absolute; inset: 0;
    background: linear-gradient(100deg, var(--wood-dark), var(--wood-light) 55%, var(--wood-dark));
  }
  .front-mark {
    position: absolute; left: 0; right: 0; top: 95px;
    text-align: center; color: var(--white);
    font-size: 76px; letter-spacing: 10px;
  }
  .tagline {
    position: absolute; left: 0; right: 0; top: 300px;
    text-align: center; color: var(--white);
    font-size: 27px; letter-spacing: 1px;
  }

  /* Back face */
  .card-back { top: 439px; background: var(--card-white); color: var(--ink-gray); }
  .corner-ornament {
    position: absolute; background: radial-gradient(ellipse at center, var(--ornament-gray), rgba(201,201,201,0) 70%);
  }
  .corner-top-left { left: -20px; top: -20px; width: 110px; height: 80px; }
  .corner-bottom-right { right: -20px; bottom: -20px; width: 150px; height: 90px; }
  .wordmark {
    position: absolute; left: 90px; top: 26px;
    font-size: 27px; letter-spacing: 1px; text-transform: uppercase;
  }
  .website { position: absolute; left: 110px; top: 66px; font-size: 20px; }
  .firm-type {
    position: absolute; right: 24px; top: 18px; width: 170px;
    text-align: center; font-size: 19px; line-height: 30px; color: var(--ink-soft);
  }
  .firm-amp {
    display: block; font-family: "Pinyon Script", cursive; font-size: 32px; line-height: 30px;
    color: var(--amp-yellow);
  }
  .name-band {
    position: absolute; left: 0; right: 0; top: 114px; height: 70px;
    background: var(--band-yellow);
  }
  .owner-name { position: absolute; left: 110px; top: 118px; font-size: 27px; }
  .owner-title { position: absolute; left: 110px; top: 152px; font-size: 20px; color: var(--ink-soft); }
  .contact-list { position: absolute; left: 48px; top: 200px; list-style: none; }
  .contact-list li { font-size: 23px; line-height: 34px; }
  .contact-letter { font-family: "Pinyon Script", cursive; font-size: 30px; margin-right: 4px; }
  .social-list {
    position: absolute; left: 48px; top: 310px;
    display: grid; grid-template-columns: 250px 260px; row-gap: 12px; list-style: none;
  }
  .social-list li {
    display: flex; align-items: center; gap: 8px;
    font-family: "Pinyon Script", cursive; font-size: 25px; color: var(--ink-soft);
  }
  .social-dot { width: 20px; height: 20px; border-radius: 50%; background: var(--ink-soft); flex: none; }
</style>
</head>
<body>
  <section class="card card-front">
    <div class="wood-texture" role="img" aria-label="Gray wood-grain plank background"></div>
    <div class="front-mark">HCW</div>
    <p class="tagline">Gather with Care. Care to Share. Share the Joy</p>
  </section>

  <section class="card card-back">
    <div class="corner-ornament corner-top-left" role="img" aria-label="Gray interlaced ring ornament in the corner"></div>
    <div class="corner-ornament corner-bottom-right" role="img" aria-label="Gray interlaced ring ornament in the corner"></div>
    <div class="wordmark">The Hollow Crest Workshop</div>
    <div class="website">www.myhollowcrestworkshop.example</div>
    <div class="firm-type">Event Planning<span class="firm-amp">&amp;</span>Design Firm</div>
    <div class="name-band"></div>
    <div class="owner-name">Odette M. Vance, Owner/CEO</div>
    <div class="owner-title">Certified Event &amp; Wedding Planner</div>
    <ul class="contact-list">
      <li><span class="contact-letter">T:</span>(555) 240-7318</li>
      <li><span class="contact-letter">F:</span>(555) 617-4052</li>
      <li><span class="contact-letter">E:</span>wegather@myhollowcrestworkshop.example</li>
    </ul>
    <ul class="social-list">
      <li><span class="social-dot"></span>@hollowcrestwork1</li>
      <li><span class="social-dot"></span>@thehollowcrestwork</li>
      <li><span class="social-dot"></span>@hollowcrestwork</li>
      <li><span class="social-dot"></span>@thehollowcrestwork1</li>
    </ul>
  </section>
</body>
</html>
```